Brindmoor Gardening Fresh New Website

We are looking to create a simple fresh website for our landscaping business. The website should appeal to a 'high end' audience. We deal with a lot of Embassies and affluent clients who have extremely large gardens that are meticulously maintained. The site is about communicating our excellent landscaping and customer service skills and encouraging new clients to reach out and engage us to take care of their gardens.

The website is basically going to be our business card, it will have almost no functionality other than two 'contact us' forms, one for smaller clients and one for more detailed projects.

The website will not have a lot of written content and will have to show photos of beautifully landscaped gardens.

The main logo in black will influence the site, however, we are open to all suggestions.

We are expecting to have the following pages:
Home Page
Services
About Us
Contact Us
Showcase (photo gallery of our work)

We need someone who can code it to wordpress and be available for minor changes over a number of days. They will be simple tweaks.

```html
<!DOCTYPE html>
<html lang="en">
<head>
<meta charset="utf-8">
<title>Brindmoor Gardening</title>
<link rel="stylesheet" href="https://fonts.googleapis.com/css2?family=Poppins:ital,wght@0,400;0,500;0,600;0,700;1,600&display=swap">
<style>
:root{
  --gold:#a36a1f;
  --gold-deep:#8a5512;
  --yellow:#e3b520;
  --ink:#1d1d1b;
  --body:#3a3a3a;
  --cream:#fdf0de;
  --dark:#1b1b19;
  --line:#d9d9d9;
  --white:#ffffff;
}
*{box-sizing:border-box;margin:0;padding:0}
html,body{width:1200px;height:4648px;overflow:hidden}
body{position:relative;background:var(--white);font-family:"Poppins",sans-serif;color:var(--body)}
.abs{position:absolute}
.btn{position:absolute;display:flex;align-items:center;justify-content:center;background:var(--gold);color:var(--white);font-size:12px;font-weight:600;text-transform:uppercase;border-radius:4px;letter-spacing:.2px}
.section-title{position:absolute;left:0;width:1200px;text-align:center;font-size:34px;font-weight:700;color:var(--ink)}
.section-title span{color:var(--gold-deep)}
.lorem{font-size:13.4px;line-height:21.2px;color:var(--body)}

/* hero */
.hero{left:0;top:0;width:1200px;height:672px;background:linear-gradient(180deg,#2b3a1c 0%,#3f5a24 35%,#5c8a2c 65%,#3d6a1e 100%)}
.hero-shade{left:0;top:0;width:1200px;height:672px;background:linear-gradient(90deg,rgba(10,14,6,.55) 0%,rgba(10,14,6,.25) 55%,rgba(0,0,0,0) 100%)}
.nav-line{left:0;width:1200px;height:1.5px;background:var(--yellow)}
.brand{left:141px;top:15px;width:122px;height:122px;border:2px solid var(--yellow);border-radius:50%;background:rgba(20,20,10,.35);display:flex;align-items:center;justify-content:center;color:var(--yellow);font-size:11.5px;font-weight:500;letter-spacing:2px;text-align:center;line-height:16px;text-transform:uppercase}
.nav{top:65px;color:var(--white);font-size:14px}
.nav-cta{left:948px;top:58px;width:112px;height:36px;background:var(--yellow);font-size:11.5px;font-weight:500;border-radius:3px}
.hero-title{left:141px;top:250px;color:var(--white);font-size:46px;font-weight:700;line-height:62px}
.hero-title span{color:var(--yellow)}
.hero-sub{left:141px;top:316px;color:var(--white);font-size:50px;font-weight:600}
.hero-text{left:141px;top:396px;width:560px;color:var(--white);font-size:13px;line-height:21px}
.hero-btn{left:141px;top:487px;width:112px;height:36px;background:var(--white);color:var(--ink);font-weight:500}
.mouse{left:567px;top:599px;width:66px;height:66px;border-radius:50%;background:var(--white);box-shadow:0 4px 14px rgba(0,0,0,.18);display:flex;align-items:center;justify-content:center}

/* about */
.about-photo{left:141px;top:753px;width:454px;height:454px;border-radius:50%;background:linear-gradient(180deg,#cfd6d6 0%,#e6dfcf 38%,#6f8a4a 62%,#8d7a66 100%)}
.about-title{left:668px;top:784px;font-size:24px;font-weight:600;color:var(--ink)}
.about-title span{color:var(--gold-deep)}
.about-text{left:664px;top:832px;width:394px}

/* services */
.services-bg{left:0;top:1312px;width:1200px;height:664px;background:linear-gradient(180deg,#eef1ea 0%,#f4f6f0 50%,#e7ece1 100%)}
.card{position:absolute;top:1505px;width:218px;height:255px;border-radius:12px;overflow:hidden;color:var(--white);text-align:center}
.card-photo{position:absolute;inset:0}
.card-shade{position:absolute;inset:0;background:linear-gradient(180deg,rgba(0,0,0,0) 35%,rgba(0,0,0,.6) 100%)}
.card h3{position:absolute;left:0;right:0;top:136px;font-size:15px;font-weight:600}
.card p{position:absolute;left:22px;right:22px;top:164px;font-size:11px;line-height:18px}
.card a{position:absolute;left:0;right:0;top:206px;font-size:11px;font-weight:600;color:var(--white);text-decoration:underline}

/* gallery */
.tile{position:absolute;width:292px;height:292px;border-radius:14px}

/* testimonials */
.testi-card{position:absolute;top:3108px;width:292px;height:284px;background:var(--white);border-radius:14px;box-shadow:0 4px 18px rgba(0,0,0,.05);padding:26px 28px}
.stars{color:var(--yellow);font-size:17px;letter-spacing:5px}
.g-dot{position:absolute;right:28px;top:28px;width:22px;height:22px;border-radius:50%;border:3px solid #4a86e8}
.testi-card p{margin-top:18px;font-size:12.5px;line-height:21.5px;color:var(--body)}
.testi-card h4{margin-top:12px;font-size:15px;font-style:italic;font-weight:600;color:var(--ink)}
.arrow{position:absolute;top:3222px;width:54px;height:54px;border-radius:50%;display:flex;align-items:center;justify-content:center}

/* contact */
.contact-card{left:141px;top:3635px;width:917px;height:428px;background:var(--white);border-radius:20px;box-shadow:0 6px 26px rgba(0,0,0,.06)}
.contact-panel{left:141px;top:3635px;width:334px;height:428px;border-radius:20px;background:linear-gradient(160deg,#2a2a26 0%,#151513 60%,#2b2616 100%);color:var(--white)}
.contact-panel .kicker{position:absolute;left:35px;top:60px;color:var(--yellow);font-size:12px;font-weight:500}
.contact-panel h2{position:absolute;left:35px;top:88px;font-size:24px;font-weight:500;line-height:38px}
.contact-row{position:absolute;left:35px;display:flex;align-items:center;gap:14px;font-size:12.5px;line-height:21px}
.icon-ring{flex:none;width:30px;height:30px;border:1.5px solid var(--white);border-radius:50%;display:flex;align-items:center;justify-content:center}
.form-title{left:514px;top:3670px;font-size:15px;font-weight:600;color:var(--ink)}
.field{position:absolute;border:1px solid #dedede;font-size:11.5px;color:#555;padding:9px 16px}
.field.active{border:2px solid #d9b58a}

/* footer */
.footer{left:0;top:4190px;width:1200px;height:458px;background:linear-gradient(180deg,#2a2a27 0%,#1b1b19 60%,#121211 100%)}
.footer-brand{left:516px;top:4193px;width:170px;height:170px;border-radius:50%;background:#1b1b19;border:3px solid var(--yellow);display:flex;align-items:center;justify-content:center;color:var(--yellow);font-size:16px;font-weight:500;letter-spacing:3px;text-align:center;line-height:22px;text-transform:uppercase}
.footer-nav{top:4418px;color:var(--white);font-size:14px}
.footer-rule{left:141px;width:917px;height:1px;background:#777}
.footer-info{position:absolute;top:4503px;display:flex;gap:12px;align-items:center;color:var(--white);font-size:12px;line-height:19px}
.copyright{left:0;width:1200px;top:4588px;text-align:center;color:var(--white);font-size:12px}
</style>
</head>
<body>

<!-- hero -->
<div class="abs hero" role="img" aria-label="Photo of a manicured garden lawn with rounded shrubs and flowering hedges"></div>
<div class="abs hero-shade"></div>
<div class="abs nav-line" style="top:43px"></div>
<div class="abs nav-line" style="top:106px"></div>
<div class="abs brand">Brindmoor<br>Gardening</div>
<div class="abs nav" style="left:589px">Home</div>
<div class="abs nav" style="left:661px">About Us</div>
<div class="abs nav" style="left:753px">Services</div>
<div class="abs nav" style="left:841px">Our Gallery</div>
<div class="btn nav-cta">Contact Us</div>
<div class="abs hero-title">BRINDMOOR <span>LANDSCAPING</span></div>
<div class="abs hero-sub">Gardening</div>
<p class="abs hero-text">Lorem ipsum dolor sit amet, consectetur adipiscing elit, sed do eiusmod tempor incid-idunt ut labore et dolore magna aliqua. Quis ipsum suspendisse ultrices gravida. Risus commodo viverra maecenas accumsan lacus vel facilisis.</p>
<div class="btn hero-btn">Read More</div>
<svg class="abs" style="left:0;top:620px" width="1200" height="60" viewBox="0 0 1200 60" preserveAspectRatio="none">
  <path d="M0 52 Q600 -8 1200 52 L1200 60 L0 60 Z" fill="#fff"/>
</svg>
<div class="abs mouse">
  <svg width="20" height="32" viewBox="0 0 20 32"><rect x="2" y="2" width="16" height="28" rx="8" fill="none" stroke="#1d1d1b" stroke-width="2"/><line x1="10" y1="8" x2="10" y2="14" stroke="#1d1d1b" stroke-width="2" stroke-linecap="round"/></svg>
</div>

<!-- about -->
<div class="abs about-photo" role="img" aria-label="Photo of a park bench beside a railing and lamp post under a cloudy sky"></div>
<h2 class="abs about-title">About <span>Us</span></h2>
<div class="abs about-text lorem">
  <p>Lorem ipsum dolor sit amet, consectetur adipiscing elit, sed do eiusmod tempor incididunt ut labore et dolore magna aliqua. Quis ipsum suspendisse ultrices gravida. Risus com-modo viverra maecenas accumsan lacus vel facilisis. Lorem ipsum dolor sit amet, consectetur adipiscing elit, sed do eiusmod tempor incididunt ut labore et dolore magna aliqua. Quis ipsum suspendisse ultrices gravida. Risus com-modo viverra maecenas accumsan lacus vel facilisis.</p>
  <p style="margin-top:21px">Lorem ipsum dolor sit amet, consectetur adipiscing elit, sed do eiusmod tempor incididunt ut labore et dolore magna aliqua. Quis ipsum suspendisse ultrices gravida. Risus com-modo viverra maecenas accumsan lacus vel facilisis.</p>
</div>
<div class="btn" style="left:664px;top:1130px;width:112px;height:38px">Read More</div>

<!-- services -->
<div class="abs services-bg" role="img" aria-label="Faded background photo of a park with trees"></div>
<svg class="abs" style="left:0;top:1300px" width="1200" height="40" viewBox="0 0 1200 40" preserveAspectRatio="none"><path d="M0 0 L1200 0 L1200 12 Q600 -10 0 12 Z" fill="#fff"/></svg>
<h2 class="section-title" style="top:1414px">Our <span>Services</span></h2>

<div class="card" style="left:141px">
  <div class="card-photo" role="img" aria-label="Photo of a single tree on a lawn at dusk" style="background:linear-gradient(180deg,#3e4a52 0%,#364a2a 55%,#2c3b1e 100%)"></div>
  <div class="card-shade"></div>
  <h3>Landscaping</h3><p>Lorem ipsum dolor sit amet, consectetur adipiscing.</p><a>Read More</a>
</div>
<div class="card" style="left:374px">
  <div class="card-photo" role="img" aria-label="Photo of hedge trimming shears cutting green leaves" style="background:linear-gradient(180deg,#4a5a3a 0%,#3a5226 55%,#2e3f1f 100%)"></div>
  <div class="card-shade"></div>
  <h3>Lawn Service</h3><p>Lorem ipsum dolor sit amet, consectetur adipiscing.</p><a>Read More</a>
</div>
<div class="card" style="left:607px">
  <div class="card-photo" role="img" aria-label="Photo of a gardener carrying a tray of grass clippings" style="background:linear-gradient(180deg,#3d4a55 0%,#55603a 55%,#2f3626 100%)"></div>
  <div class="card-shade"></div>
  <h3>Lawn Maintenance</h3><p>Lorem ipsum dolor sit amet, consectetur adipiscing.</p><a>Read More</a>
</div>
<div class="card" style="left:839px">
  <div class="card-photo" role="img" aria-label="Photo of tree care workers in safety vests among trees" style="background:linear-gradient(180deg,#4a4236 0%,#6a4a2a 55%,#3a3226 100%)"></div>
  <div class="card-shade"></div>
  <h3>Tree Services</h3><p>Lorem ipsum dolor sit amet, consectetur adipiscing.</p><a>Read More</a>
</div>
<div class="btn" style="left:518px;top:1811px;width:164px;height:38px">View All Services</div>
<svg class="abs" style="left:0;top:1924px" width="1200" height="54" viewBox="0 0 1200 54" preserveAspectRatio="none"><path d="M0 54 L0 44 Q600 -10 1200 44 L1200 54 Z" fill="#fff"/></svg>

<!-- gallery -->
<h2 class="section-title" style="top:2039px">Our <span>Gallery</span></h2>
<div class="tile" style="left:141px;top:2141px;background:linear-gradient(160deg,#5f8f35,#3f6a26 60%,#6b6f66)" role="img" aria-label="Photo of a wooden boardwalk through green park trees"></div>
<div class="tile" style="left:453px;top:2141px;background:linear-gradient(180deg,#5a7a2e,#6e9a3a 55%,#8c8a82)" role="img" aria-label="Photo of a path under green arches of climbing plants"></div>
<div class="tile" style="left:765px;top:2141px;background:linear-gradient(180deg,#2f8ee0 0%,#7fc0ef 40%,#c43b2a 62%,#5aa62e 78%)" role="img" aria-label="Photo of red flower beds on a bright lawn under blue sky"></div>
<div class="tile" style="left:141px;top:2451px;background:linear-gradient(180deg,#b5a28a 0%,#b07a3a 40%,#6a9a35 70%,#e8e8e8 100%)" role="img" aria-label="Photo of an autumn park with a white picket fence and bench"></div>
<div class="tile" style="left:453px;top:2451px;background:linear-gradient(180deg,#2e4a24 0%,#9ab0a8 35%,#5f9a2e 65%,#8a7a62 100%)" role="img" aria-label="Photo of stepping stone path across a lawn toward a waterfall"></div>
<div class="tile" style="left:765px;top:2451px;background:linear-gradient(180deg,#3e5a2a 0%,#a8a59a 45%,#4f8a2a 75%,#9a958a 100%)" role="img" aria-label="Photo of a stone gazebo surrounded by clipped round shrubs"></div>
<div class="btn" style="left:525px;top:2792px;width:150px;height:38px">View All Gallery</div>

<!-- testimonials -->
<div class="abs" style="left:0;top:2890px;width:1200px;height:640px;background:var(--cream)"></div>
<svg class="abs" style="left:0;top:2880px" width="1200" height="50" viewBox="0 0 1200 50" preserveAspectRatio="none"><path d="M0 0 L1200 0 L1200 16 Q600 -12 0 32 Z" fill="#fff"/></svg>
<svg class="abs" style="left:0;top:3480px" width="1200" height="56" viewBox="0 0 1200 56" preserveAspectRatio="none"><path d="M0 56 L0 40 Q600 -20 1200 40 L1200 56 Z" fill="#fff"/></svg>
<h2 class="section-title" style="top:3010px">Client <span>Testimonials</span></h2>

<div class="testi-card" style="left:141px"><div class="stars">★★★★★</div><span class="g-dot"></span>
  <p>Lorem ipsum dolor sit amet, consecte-tur adipiscing elit, sed do eiusmod tempor incididunt ut labore et dolore magna aliqua. Quis ipsum sus-pendisse ultrices gravida. Risus com-modo viverra maecenas accumsan lacus vel facilisis.</p><h4>Marta Velden</h4></div>
<div class="testi-card" style="left:453px"><div class="stars">★★★★★</div><span class="g-dot"></span>
  <p>Lorem ipsum dolor sit amet, consecte-tur adipiscing elit, sed do eiusmod tempor incididunt ut labore et dolore magna aliqua. Quis ipsum sus-pendisse ultrices gravida. Risus com-modo viverra maecenas accumsan lacus vel facilisis.</p><h4>Marta Velden</h4></div>
<div class="testi-card" style="left:765px"><div class="stars">★★★★★</div><span class="g-dot"></span>
  <p>Lorem ipsum dolor sit amet, consecte-tur adipiscing elit, sed do eiusmod tempor incididunt ut labore et dolore magna aliqua. Quis ipsum sus-pendisse ultrices gravida. Risus com-modo viverra maecenas accumsan lacus vel facilisis.</p><h4>Marta Velden</h4></div>

<div class="arrow" style="left:64px;border:2px solid var(--gold)"><svg width="16" height="24" viewBox="0 0 16 24"><path d="M12 3 L4 12 L12 21" fill="none" stroke="#a36a1f" stroke-width="2.5" stroke-linecap="round" stroke-linejoin="round"/></svg></div>
<div class="arrow" style="left:1080px;background:var(--gold)"><svg width="16" height="24" viewBox="0 0 16 24"><path d="M4 3 L12 12 L4 21" fill="none" stroke="#fff" stroke-width="2.5" stroke-linecap="round" stroke-linejoin="round"/></svg></div>

<!-- contact -->
<div class="abs contact-card"></div>
<div class="abs contact-panel" role="img" aria-label="Dark photo of a garden at dusk behind contact details">
  <div class="kicker">CONTACT US</div>
  <h2>Ask One Of Our<br>Experts For Help</h2>
  <div class="contact-row" style="top:183px"><span class="icon-ring"><svg width="14" height="14" viewBox="0 0 24 24"><path d="M6 2 L10 7 L8 10 Q10 14 14 16 L17 14 L22 18 L19 22 Q9 21 2 5 Z" fill="none" stroke="#fff" stroke-width="2" stroke-linejoin="round"/></svg></span>+1 555-014-2290</div>
  <div class="contact-row" style="top:236px"><span class="icon-ring"><svg width="14" height="12" viewBox="0 0 24 18"><rect x="1" y="1" width="22" height="16" rx="2" fill="#fff"/><path d="M2 2 L12 10 L22 2" fill="none" stroke="#1b1b19" stroke-width="2"/></svg></span>hello@brindmoorgardens.com</div>
  <div class="contact-row" style="top:285px"><span class="icon-ring"><svg width="12" height="15" viewBox="0 0 20 26"><path d="M10 1 C4 1 1 5 1 10 C1 16 10 25 10 25 C10 25 19 16 19 10 C19 5 16 1 10 1 Z" fill="none" stroke="#fff" stroke-width="2.2"/><circle cx="10" cy="10" r="3" fill="#fff"/></svg></span>Lorem Ipsum is simply of the<br>printing and typesetting industry.</div>
</div>
<div class="abs form-title">DROP YOUR MESSAGE</div>
<div class="field active" style="left:514px;top:3723px;width:248px;height:36px">First Name</div>
<div class="field" style="left:772px;top:3723px;width:248px;height:36px">Last Name</div>
<div class="field" style="left:514px;top:3772px;width:248px;height:36px">Email Address</div>
<div class="field" style="left:772px;top:3772px;width:248px;height:36px">Phone</div>
<div class="field" style="left:514px;top:3822px;width:506px;height:137px">Message</div>
<div class="btn" style="left:514px;top:3986px;width:129px;height:38px">Submit Now</div>

<!-- footer -->
<div class="abs footer" role="img" aria-label="Dark faded photo of trees behind the footer"></div>
<svg class="abs" style="left:0;top:4188px" width="1200" height="40" viewBox="0 0 1200 40" preserveAspectRatio="none"><path d="M0 0 L1200 0 L1200 30 Q600 -6 0 30 Z" fill="#fff"/></svg>
<div class="abs footer-brand">Brindmoor<br>Gardening</div>
<div class="abs footer-nav" style="left:377px">Home</div>
<div class="abs footer-nav" style="left:450px">About Us</div>
<div class="abs footer-nav" style="left:543px">Services</div>
<div class="abs footer-nav" style="left:631px">Our Gallery</div>
<div class="abs footer-nav" style="left:741px">Contact Us</div>
<div class="abs footer-rule" style="top:4478px"></div>
<div class="footer-info" style="left:141px"><svg width="22" height="22" viewBox="0 0 24 24"><circle cx="12" cy="12" r="10" fill="none" stroke="#fff" stroke-width="1.5"/><ellipse cx="12" cy="12" rx="4.5" ry="10" fill="none" stroke="#fff" stroke-width="1.5"/><line x1="2" y1="12" x2="22" y2="12" stroke="#fff" stroke-width="1.5"/></svg><span>Lorem Ipsum is simply dummy text<br>of the printing and typesetting.</span></div>
<div class="footer-info" style="left:506px"><svg width="22" height="22" viewBox="0 0 24 24"><path d="M6 2 L10 7 L8 10 Q10 14 14 16 L17 14 L22 18 L19 22 Q9 21 2 5 Z" fill="none" stroke="#fff" stroke-width="1.5" stroke-linejoin="round"/></svg><span>Call Us<br>+1 555-014-2290</span></div>
<div class="footer-info" style="left:797px"><svg width="22" height="20" viewBox="0 0 24 20"><rect x="1" y="2" width="22" height="16" rx="2" fill="none" stroke="#fff" stroke-width="1.5"/><path d="M2 3 L12 11 L22 3" fill="none" stroke="#fff" stroke-width="1.5"/></svg><span>Email<br>hello@brindmoorgardens.com</span></div>
<div class="abs footer-rule" style="top:4561px"></div>
<div class="abs copyright">© 2024 Brindmoor Landscaping Gardening. All Rights Reserved.</div>

</body>
</html>
```